CTWI application splash screen

We need a 1024x768 image for use as an application splash screen.
The image will be displayed full screen on an 10 inch industrial PC 1024x768 screen while our application is launching. The image should convey that the application is "Waiting for connection to Wi-Fi access point..." and include a graphic of the industrial PC connected to the access point via an Ethernet cable. A list of troubleshooting steps should be included at the bottom of the image. The troubleshooting steps should not be the main focus of the image and should be shown in a smaller font (but still readable at 1024x768 displayed on a 10 inch screen).
I will include a mock up of the general idea of what we are looking for as well as image files for the industrial PC, a screenshot of our application to show on the PC's screen and the AP.
For general look and feel and a sense of corporate branding please review our website https://corvanetillageworks.com/. The splash screen should reflect corporate branding.
Target Market(s)
Users of our application
Industry/Entity Type
Agriculture

```html
<!DOCTYPE html>
<html lang="en">
<head>
<meta charset="utf-8">
<title>CTWI Splash Screen</title>
<link rel="stylesheet" href="https://fonts.googleapis.com/css2?family=Poppins:wght@300;400;500;700;800&display=swap">
<style>
  :root {
    --page-bg: #e6e6e6;
    --green-light: #5caf77;
    --green-dark: #3f8d5c;
    --green-pill: #6cbd88;
    --check-green: #49a866;
    --ink: #1c1c1c;
    --text: #222222;
    --white: #ffffff;
    --device: #262626;
    --cable-tone: #2c3a31;
    --ap-body: #f2f4f3;
  }
  * { margin: 0; padding: 0; box-sizing: border-box; }
  html, body {
    width: 1200px; height: 1200px; overflow: hidden;
    background: var(--page-bg);
    font-family: "Poppins", sans-serif;
  }
  .splash {
    position: absolute; left: 0; top: 150px;
    width: 1200px; height: 900px; overflow: hidden;
    background: linear-gradient(160deg, var(--green-light) 0%, var(--green-dark) 100%);
  }
  .splash__lower {
    position: absolute; inset: 0; width: 1200px; height: 900px;
  }
  .device-illustration {
    position: absolute; left: 122px; top: 67px; width: 361px; height: 287px;
    background: var(--device); border-radius: 18px;
  }
  .cable-illustration {
    position: absolute; left: 483px; top: 165px; width: 535px; height: 200px;
    background: linear-gradient(90deg, #2f4034 0%, var(--cable-tone) 100%);
    border-radius: 14px; opacity: 0.85;
  }
  .ap-illustration {
    position: absolute; left: 1018px; top: 27px; width: 44px; height: 334px;
    background: var(--ap-body); border-radius: 10px;
  }
  .label-pill {
    position: absolute; height: 34px; padding: 0 12px;
    border-radius: 17px; background: var(--green-pill);
    color: var(--white); font-size: 19px; font-weight: 400;
    line-height: 34px; white-space: nowrap; letter-spacing: 0.2px;
  }
  .label-pill--computer { left: 490px; top: 108px; }
  .label-pill--ap { left: 804px; top: 55px; }
  .headline {
    position: absolute; left: 69px; top: 393px;
    color: var(--white); font-weight: 300; font-size: 58px;
    line-height: 56px; letter-spacing: -0.5px; white-space: nowrap;
  }
  .steps-heading {
    position: absolute; left: 60px; top: 541px; height: 36px; padding: 0 20px;
    border-radius: 18px; background: var(--ink); color: var(--white);
    font-weight: 700; font-size: 23px; line-height: 37px; white-space: nowrap;
  }
  .steps { position: absolute; left: 0; top: 0; width: 1200px; height: 900px; }
  .step {
    position: absolute; color: var(--text); font-size: 18px; font-weight: 400;
    line-height: 24px; white-space: nowrap;
  }
  .brand {
    position: absolute; left: 900px; top: 770px; width: 270px; text-align: center;
    color: var(--ink); font-weight: 700; white-space: nowrap;
  }
  .brand__mark { font-size: 64px; line-height: 64px; letter-spacing: 2px; }
  .brand__name { font-size: 17px; line-height: 24px; margin-top: 6px; }
</style>
</head>
<body>
<main class="splash">
  <svg class="splash__lower" viewBox="0 0 1200 900" aria-hidden="true">
    <polygon points="0,540 1200,635 1200,900 0,900" fill="#ffffff"/>
  </svg>

  <div class="device-illustration" role="img" aria-label="Tractor cab computer showing the seeding application"></div>
  <div class="cable-illustration" role="img" aria-label="Coiled Ethernet cable linking the computer to the access point"></div>
  <div class="ap-illustration" role="img" aria-label="Wi-Fi access point with two antennas"></div>

  <div class="label-pill label-pill--computer">TRACTOR CAB COMPUTER</div>
  <div class="label-pill label-pill--ap">WI-FI ACCESS POINT</div>

  <h1 class="headline">WAITING FOR CONNECTION TO<br>WI-FI ACCESS POINT...</h1>

  <div class="steps-heading">TROUBLESHOOTING STEPS:</div>

  <svg class="steps" viewBox="0 0 1200 900" aria-hidden="true">
    <g stroke="#49a866" stroke-width="1.6" fill="none">
      <line x1="71" y1="590" x2="71" y2="813"/>
      <line x1="104" y1="663" x2="104" y2="849"/>
    </g>
    <g fill="#ffffff" stroke="#49a866" stroke-width="2" stroke-linecap="round" stroke-linejoin="round">
      <g transform="translate(71,612)"><circle r="10"/><path d="M-5,0 L-1,4 L8,-7" fill="none"/></g>
      <g transform="translate(71,646)"><circle r="10"/><path d="M-5,0 L-1,4 L8,-7" fill="none"/></g>
      <g transform="translate(104,690)"><circle r="10"/><path d="M-5,0 L-1,4 L8,-7" fill="none"/></g>
      <g transform="translate(104,747)"><circle r="10"/><path d="M-5,0 L-1,4 L8,-7" fill="none"/></g>
      <g transform="translate(104,803)"><circle r="10"/><path d="M-5,0 L-1,4 L8,-7" fill="none"/></g>
      <g transform="translate(104,836)"><circle r="10"/><path d="M-5,0 L-1,4 L8,-7" fill="none"/></g>
    </g>
  </svg>

  <p class="step" style="left:91px; top:600px;">This screen should only be visible for a short time on boot.</p>
  <p class="step" style="left:89px; top:634px;">If this screen stays visible for more than a minute:</p>
  <p class="step" style="left:128px; top:676px;">Verify that the Wi-Fi Access Point (AP) powers up when this system does<br>(indicated by a green light on the side of the AP).</p>
  <p class="step" style="left:128px; top:733px;">Check the Ethernet cable between this system and the AP for damage<br>and replace it if necessary.</p>
  <p class="step" style="left:127px; top:791px;">Power-cycle this system and wait for it to reboot fully.</p>
  <p class="step" style="left:127px; top:824px;">If the issue persists, contact CTWI support for further assistance.</p>

  <div class="brand">
    <div class="brand__mark">CTWI</div>
    <div class="brand__name">Corvane Tillage Works Inc.</div>
  </div>
</main>
</body>
</html>
```